I need a business card design for my new clinic (SPORTS MEDICINE OF KNEE). I am orthopedist, expert in sports surgery, especially knee surgery. I prefer, as colors, the colors of my logo (green, black and white). I already have my logo and should appear on my card. It's good to see my site to have ideas (www.drlucianovarela.com)
It needs contain:
my name: Dr. Luciano Varela
my registration: CRM 584-902
my specialty: Cirurgia do Joelho / Esporte
my address: Centro Executivo - Pinheiral Plaza
Av. Doutor Augusto Brandão Cunha, 2740 sala 0836
Jd. Ipanema - Ribeirão Preto - SP
my phone number: Tel (16) 8245-3908
my clinic phone: (16) 3670-4851
my e-mail: drlucianovarela@mailbox-exemplo.com
my site: www.drlucianovarela.com

Target Market(s)

futures patients

Industry/Entity Type

Clinic

Requirements
Nice to have
• letters not overfilled
straight lines, with few curves

```html
<!DOCTYPE html>
<html lang="pt-BR">
<head>
<meta charset="utf-8">
<title>Dr. Luciano Varela — Cartão de Visita</title>
<link rel="stylesheet" href="https://fonts.googleapis.com/css2?family=Crimson+Pro:wght@400;700&family=Roboto+Condensed:wght@400&family=Arimo:wght@400&family=Encode+Sans+Condensed:wght@700&family=Lato:wght@900&display=swap">
<style>
  :root {
    --page: #ffffff;
    --card: #2b2f2e;
    --card-mid: #222524;
    --card-dark: #111312;
    --green: #5cf046;
    --green-light: #a9f79c;
    --text: #ffffff;
    --text-soft: #e6efe4;
  }
  * { margin: 0; padding: 0; box-sizing: border-box; }
  html, body { width: 1200px; height: 892px; overflow: hidden; background: var(--page); }
  .canvas { position: relative; width: 1200px; height: 892px; }
  .card {
    position: absolute; left: 131px; top: 131px; width: 936px; height: 628px;
    overflow: hidden; background: var(--card);
  }
  .card-shapes { position: absolute; inset: 0; }
  .brand-tile {
    position: absolute; left: 15px; top: 11px; width: 139px; height: 130px;
    display: flex; flex-direction: column; align-items: center; justify-content: center; gap: 10px;
  }
  .brand-tile .square { width: 58px; height: 58px; background: var(--green); border-radius: 6px; }
  .brand-tile .brand-name {
    font-family: "Crimson Pro", serif; font-weight: 700; font-size: 24px; color: var(--text);
  }
  .doctor { position: absolute; left: 168px; top: 16px; color: var(--text); font-family: "Crimson Pro", serif; }
  .doctor .name { font-weight: 700; font-size: 45px; line-height: 1; letter-spacing: 0.3px; }
  .doctor .specialty { font-weight: 400; font-size: 27px; line-height: 1; margin-top: 6px; }
  .doctor .registration { font-weight: 400; font-size: 22px; line-height: 1; margin-top: 8px; color: var(--text-soft); }
  .clinic { position: absolute; left: 543px; top: 212px; color: var(--text); }
  .clinic .clinic-name { font-family: "Lato", sans-serif; font-weight: 900; font-size: 27px; letter-spacing: 0.5px; line-height: 1; }
  .clinic .address { font-family: "Roboto Condensed", sans-serif; font-size: 24px; line-height: 28.5px; margin-top: 14px; }
  .phones { position: absolute; left: 549px; top: 380px; color: var(--text); font-family: "Arimo", sans-serif; font-size: 27px; line-height: 42px; }
  .phones .second { padding-left: 63px; }
  .email { position: absolute; right: 12px; top: 470px; color: var(--text); font-family: "Arimo", sans-serif; font-size: 20px; line-height: 1.2; }
  .website {
    position: absolute; right: 29px; top: 558px; color: var(--text);
    font-family: "Encode Sans Condensed", sans-serif; font-weight: 700; font-size: 35px; line-height: 1;
  }
</style>
</head>
<body>
<div class="canvas">
  <div class="card">
    <svg class="card-shapes" width="936" height="628" viewBox="0 0 936 628" aria-hidden="true">
      <path d="M532 0 H936 V210 C880 110 720 40 532 0 Z" fill="var(--green)"/>
      <path d="M532 0 C720 40 880 110 936 210 V236 C870 120 720 40 532 0 Z" fill="var(--green-light)"/>
      <path d="M0 480 C300 488 560 505 1000 540 V628 H0 Z" fill="var(--card-mid)"/>
      <rect x="0" y="514" width="936" height="114" fill="var(--card-dark)"/>
      <path d="M0 471 C260 476 520 492 680 514 L620 514 C480 500 260 488 0 483 Z" fill="var(--green)"/>
    </svg>

    <div class="brand-tile">
      <div class="square"></div>
      <div class="brand-name">Varela</div>
    </div>

    <div class="doctor">
      <div class="name">Dr. Luciano Varela</div>
      <div class="specialty">(Cirurgia do Joelho / Esporte)</div>
      <div class="registration">CRM 584-902</div>
    </div>

    <div class="clinic">
      <div class="clinic-name">CLÍNICA MOTRIX</div>
      <div class="address">
        Centro Executivo - Pinheiral Plaza<br>
        Av. Doutor Augusto Brandão Cunha,<br>
        2740&nbsp; sala 0836 ,&nbsp; Jd. Ipanema<br>
        Ribeirão Preto - SP
      </div>
    </div>

    <div class="phones">
      <div>Tel : (16) 8245-3908</div>
      <div class="second">(16) 3670-4851</div>
    </div>

    <div class="email">e-mail: drlucianovarela@mailbox-exemplo.com</div>

    <div class="website">www.drlucianovarela.com</div>
  </div>
</div>
</body>
</html>
```